*** Business Card Design Project

I need a logo and business card for my new catering business: "Pomelia". The design should be modern, clean, elegant and refined. One or Two colours only. The design SHOULD NOT include graphics or images. There should be space for my name, phone number and email address (I will provide these to you later).

Industry/Entity Type

Catering

Requirements
Must have
• Must have one or two colours only.
Must include the text "pomelia"
Should not have
• Must not have graphics or images.

```html
<!DOCTYPE html>
<html lang="en">
<head>
<meta charset="utf-8">
<title>Pomelia Catering – Business Card</title>
<link href="https://fonts.googleapis.com/css2?family=Marcellus&family=Varela+Round&family=Open+Sans:wght@400&display=swap" rel="stylesheet">
<style>
  :root {
    --backdrop-light: #ffffff;
    --backdrop-dark: #d9d9d9;
    --card-blue: #00aeef;
    --ink-white: #ffffff;
    --accent-yellow: #e6e619;
  }
  * { box-sizing: border-box; margin: 0; padding: 0; }
  html, body {
    width: 1200px;
    height: 900px;
    overflow: hidden;
  }
  body {
    background: radial-gradient(ellipse at center, var(--backdrop-light) 0%, var(--backdrop-dark) 100%);
    display: flex;
    align-items: center;
    justify-content: center;
  }
  .business-card {
    position: relative;
    width: 840px;
    height: 480px;
    background: var(--card-blue);
    color: var(--ink-white);
  }
  .brand {
    position: absolute;
    left: 0;
    right: 0;
    top: 118px;
    display: flex;
    flex-direction: column;
    align-items: center;
  }
  .brand-lockup {
    display: inline-flex;
    flex-direction: column;
    align-items: flex-end;
  }
  .brand-name {
    font-family: "Marcellus", serif;
    font-size: 104px;
    line-height: 1;
    color: var(--ink-white);
    letter-spacing: 1px;
  }
  .brand-tagline {
    font-family: "Varela Round", sans-serif;
    font-size: 36px;
    letter-spacing: 9px;
    color: var(--accent-yellow);
    margin-top: 2px;
    margin-right: -4px;
  }
  .holder-name {
    position: absolute;
    left: 0;
    right: 0;
    top: 308px;
    text-align: center;
    font-family: "Open Sans", sans-serif;
    font-size: 30px;
    color: var(--accent-yellow);
  }
  .contact-row {
    position: absolute;
    left: 0;
    right: 0;
    top: 362px;
    display: flex;
    justify-content: center;
    gap: 40px;
    font-family: "Open Sans", sans-serif;
    font-size: 21px;
    color: var(--ink-white);
  }
  .contact-item {
    display: flex;
    align-items: center;
    gap: 10px;
  }
  .contact-phone { letter-spacing: 2px; }
  .contact-icon { display: block; }
</style>
</head>
<body>
  <main class="business-card">
    <div class="brand">
      <div class="brand-lockup">
        <span class="brand-name">Pomelia</span>
        <span class="brand-tagline">catering</span>
      </div>
    </div>

    <p class="holder-name">Daniel Hart</p>

    <div class="contact-row">
      <span class="contact-item">
        <svg class="contact-icon" width="14" height="24" viewBox="0 0 14 24" aria-hidden="true">
          <rect x="1" y="1" width="12" height="22" rx="2" fill="none" stroke="var(--ink-white)" stroke-width="2"/>
          <rect x="3.5" y="4" width="7" height="10" fill="var(--ink-white)"/>
          <circle cx="7" cy="18.5" r="1.5" fill="var(--ink-white)"/>
        </svg>
        <span class="contact-phone">0198765432</span>
      </span>
      <span class="contact-item">
        <svg class="contact-icon" width="24" height="18" viewBox="0 0 24 18" aria-hidden="true">
          <rect x="1" y="1" width="22" height="16" fill="none" stroke="var(--ink-white)" stroke-width="2"/>
          <path d="M1 1 L12 10 L23 1" fill="none" stroke="var(--ink-white)" stroke-width="2"/>
        </svg>
        <span class="contact-email">DanielHart@pomelia.com</span>
      </span>
    </div>
  </main>
</body>
</html>
```